Webdesign für Fahrschule
Petra Lindqvor
Sehr ansprechendes, modernes und übersichtliches Design, welches das Unternehmen sehr gut widerspiegelt
Zielgruppe
Fahrschule mit fach- und sachgerechter Fahrschulausbildung in allen Zweiradklassen und im PKW-Bereich sowie Ausbildung auf Automatikfahrzeugen und Führerscheinausbildung für Behinderte
Aufgabenstellung
Keine Kopie der alten Seite
Nutzerfreundliche Unternehmenswebseite
Design soll frisch, modern und aussagekräftig erscheinen

```html
<!DOCTYPE html>
<html lang="de">
<head>
<meta charset="utf-8">
<title>Brandhoff Fahrschule</title>
<link href="https://fonts.googleapis.com/css2?family=Open+Sans:wght@400;600;700&family=Poppins:wght@400;500&display=swap" rel="stylesheet">
<style>
:root{
  --green:#5fa472;
  --green-dark:#4f9162;
  --ink:#3b3b3b;
  --text:#555;
  --muted:#9a9a9a;
  --grey-bg:#f3f3f3;
  --field:#f4f4f4;
  --field-line:#dcdcdc;
  --white:#fff;
  --bar:#3d3d3d;
}
*{box-sizing:border-box;margin:0;padding:0}
html,body{width:1200px;height:4209px;overflow:hidden}
body{position:relative;font-family:"Open Sans",sans-serif;color:var(--text);background:var(--white)}
.abs{position:absolute}
.btn{position:absolute;display:flex;align-items:center;justify-content:center;background:var(--green);color:#fff;font-size:15px;letter-spacing:.4px;border-radius:2px}
.ph{position:absolute}

/* hero */
.hero{position:absolute;left:0;top:0;width:1200px;height:652px;background:linear-gradient(100deg,#d9d9d9 0%,#e6e6e6 45%,#cfcfcf 100%)}
.brand{position:absolute;font-size:22px;line-height:26px;color:var(--ink)}
.brand b{display:block;color:var(--green);font-weight:700}
.nav{position:absolute;left:290px;top:29px;display:flex;gap:10px;font-size:15px;color:var(--ink)}
.hero h1{position:absolute;left:70px;top:146px;font-size:54px;line-height:82px;color:var(--green);font-weight:700;letter-spacing:.5px}
.hero p{position:absolute;left:70px;top:318px;width:390px;font-size:15px;line-height:27.5px;color:var(--ink)}

/* booking */
.booking{position:absolute;left:0;top:652px;width:1200px;height:763px;background:var(--grey-bg)}
.card{position:absolute;background:#fff;box-shadow:0 6px 30px rgba(0,0,0,.06);border-radius:4px}
.label{position:absolute;font-size:20px;font-weight:600;color:var(--ink)}
.field{position:absolute;background:var(--field);border:1px solid var(--field-line);border-radius:2px;font-size:14px;color:#aaa;padding:15px 16px}
.green-head{position:absolute;color:var(--green);font-weight:700}

/* about */
.about-text{position:absolute;left:588px;top:1702px;width:510px;font-size:14.5px;line-height:27.5px;color:var(--text)}

/* prices */
.prices{position:absolute;left:0;top:2116px;width:1200px;height:1950px;background:var(--grey-bg)}
.section-title{position:absolute;width:1200px;left:0;text-align:center;font-weight:700;color:var(--ink)}
.price{position:absolute;top:2244px;width:310px;height:444px;background:#fff;border-radius:14px;box-shadow:0 2px 12px rgba(0,0,0,.08)}
.price.featured{border:2px solid var(--green)}
.price .kicker{position:absolute;top:30px;width:100%;text-align:center;font-size:12px;color:var(--green);font-weight:600}
.price h3{position:absolute;top:44px;left:38px;right:18px;text-align:center;font-size:30px;color:var(--ink);font-weight:700;padding-bottom:4px;border-bottom:1px solid #999}
.price p{position:absolute;top:100px;left:25px;right:20px;font-size:14.5px;line-height:27.5px}
.price .btn{top:368px;left:75px;width:152px;height:48px}
.asf{position:absolute;left:118px;top:2856px;width:970px;font-size:14.5px;line-height:27.5px}
.asf p{margin-bottom:27.5px}

/* contact */
.info{position:absolute;left:172px;font-family:"Poppins",sans-serif;font-size:13px;color:var(--ink);display:flex;gap:12px;align-items:flex-start;line-height:20px}
.social{position:absolute;top:3829px;width:30px;height:30px;border-radius:50%;background:var(--green)}
.footer-nav{position:absolute;left:381px;top:4093px;display:flex;gap:22px;font-size:15px;color:var(--ink);letter-spacing:.5px}
.bar{position:absolute;left:0;top:4154px;width:1200px;height:55px;background:var(--bar);color:#fff;font-size:14px;display:flex;align-items:center;justify-content:center}
</style>
</head>
<body>

<header class="hero">
  <div class="ph" role="img" aria-label="Blasser Hintergrund: Fahrer am Lenkrad im Auto" style="left:0;top:0;width:1200px;height:652px;background:linear-gradient(110deg,rgba(255,255,255,.25),rgba(200,200,200,.2))"></div>
  <div class="brand" style="left:70px;top:16px"><b>Brandhoff</b>Fahrschule</div>
  <nav class="nav"><span>Startseite</span><span>Anmeldung</span><span>Aufbauseminar</span><span>Kontakt</span><span>Impressum</span><span>Datenschutzerklärung</span></nav>
  <div class="btn" style="left:947px;top:17px;width:153px;height:48px">Jetzt anmelden</div>
  <h1>Fahre deinen Weg –<br>Mit uns sicher ans</h1>
  <p>Individuelle Fahrerausbildung, moderne Fahrzeuge und erfahrene Fahrlehrer – wir bringen dich sicher auf die Straße. Beginne noch heute deine Reise zum Führerschein</p>
  <div class="btn" style="left:72px;top:446px;width:153px;height:48px">Jetzt anmelden</div>
  <div class="ph" role="img" aria-label="Weißer SUV in Frontansicht" style="left:640px;top:150px;width:560px;height:430px;border-radius:120px 60px 40px 80px;background:radial-gradient(ellipse at 50% 45%,#fafafa 0%,#e8e8e8 55%,#b9b9b9 85%,rgba(120,120,120,.0) 100%)"></div>
</header>

<section class="booking">
  <div class="card" style="left:100px;top:71px;width:1000px;height:644px">
    <div class="ph" role="img" aria-label="Junger Fahrschüler am Steuer mit Fahrlehrer auf dem Beifahrersitz" style="left:10px;top:10px;width:420px;height:624px;background:linear-gradient(135deg,#7d9aa6 0%,#4e6d80 45%,#2f4658 100%)"></div>
    <div class="green-head" style="left:508px;top:66px;font-size:29px;line-height:33px;width:420px">Starte Deine Fahrt – Jetzt Fahrstunden buchen!</div>
    <div class="label" style="left:508px;top:172px">Fullname</div>
    <div class="label" style="left:729px;top:172px">Email</div>
    <div class="field" style="left:508px;top:205px;width:204px;height:57px">Type name here</div>
    <div class="field" style="left:729px;top:205px;width:204px;height:57px">Type email here</div>
    <div class="label" style="left:508px;top:297px">Telefonnummer</div>
    <div class="label" style="left:729px;top:297px">Course interest</div>
    <div class="field" style="left:508px;top:330px;width:204px;height:57px">Type phone here</div>
    <div class="field" style="left:729px;top:330px;width:204px;height:57px">Type course here</div>
    <div class="label" style="left:508px;top:422px">Message</div>
    <div class="field" style="left:508px;top:455px;width:425px;height:57px">Note</div>
    <div class="btn" style="left:779px;top:540px;width:153px;height:48px">Jetzt anmelden</div>
  </div>
</section>

<section>
  <div class="ph" role="img" aria-label="Gebäude der Fahrschule mit Ladenfront an der Straße" style="left:118px;top:1526px;width:407px;height:461px;border-top-right-radius:300px 260px;background:linear-gradient(180deg,#9ec3e4 0%,#c9d8e2 30%,#d7d2c6 55%,#9a9a95 80%,#7c8a6d 100%)"></div>
  <div class="abs" style="left:594px;top:1580px;font-size:40px;font-weight:600;color:var(--ink)">Über uns</div>
  <div class="green-head" style="left:594px;top:1636px;font-size:20px;line-height:27px;width:430px">Herzlich Willkommen bei der Fahrschule Brandhoff!</div>
  <div class="about-text">
    Ihr seid auf der Suche nach einer Fahrschule die euch schnell, sicher und gut ausgebildet zum Führerschein bringt?<br>
    Dann seid Ihr hier genau richtig ! ! !<br>
    Wir bieten euch eine fach- und sachgerechte Fahrschulausbildung in allen Zweiradklassen und natürlich im PKW-Bereich.<br>
    Aber auch die Ausbildung auf Automatikfahrzeugen und die Führerscheinausbildung für Behinderte ist bei uns möglich.<br><br><br>
    Andere Termine sind nach Vereinbarung selbstverständlich möglich..<br>
    Eure Fahrschule Lukas Brandhoff
  </div>
</section>

<section class="prices"></section>
<div class="section-title" style="top:2150px;font-size:40px">Preisliste</div>

<article class="price" style="left:118px">
  <div class="kicker">PKW-Führerschein</div>
  <h3>Klasse B</h3>
  <p>Kfz bis 3500 Kg auch mit Anhänger, bis acht Sitzplätze außer Fahrersitz, Kombination aus Zugfahrzeug Klasse B und Anhänger, wobei die zulässige Gesamtmasse Anhänger und zulässige Gesamtmasse PKW nicht 3500 Kg überschreiten darf. Mindestalter 18 Jahre oder 17 Jahre in Begleitung.</p>
  <div class="btn">Jetzt anmelden</div>
</article>
<article class="price featured" style="left:456px">
  <div class="kicker">Anhängerführerschein</div>
  <h3>Klasse BE</h3>
  <p>Kombination aus Fahrzeug der Klasse B und Anhänger und Kombinationen, die nicht unter Klasse B fallen.<br><span style="display:block;height:13px"></span>Kombination aus Fahrzeug der Klasse B und Anhänger und Kombinationen, die nicht unter Klasse B fallen.</p>
  <div class="btn" style="left:73px">Jetzt anmelden</div>
</article>
<article class="price" style="left:791px">
  <div class="kicker">Motorradführerschein</div>
  <h3>Klasse A</h3>
  <p>Kfz bis 3500 Kg auch mit Anhänger, bis acht Sitzplätze außer Fahrersitz, Kombination aus Zugfahrzeug Klasse B und Anhänger, wobei die zulässige Gesamtmasse Anhänger und zulässige Gesamtmasse PKW nicht 3500 Kg überschreiten darf. Mindestalter 18 Jahre oder 17 Jahre in Begleitung.</p>
  <div class="btn">Jetzt anmelden</div>
</article>

<div class="section-title" style="top:2740px;font-size:40px">ASF - Aufbauseminar für Fahranfänger</div>
<div class="asf">
  <p>Das Aufbauseminar für Fahranfänger (ASF), auch Nachschulung genannt, ist eine von der Fahrerlaubnisbehörde (Straßenverkehrsamt) angeordnete Maßnahme bei einem A- oder zwei B-Verstößen innerhalb der Führerschein-Probezeit.</p>
  <p>Das Aufbauseminar wird von einer dazu lizenzierten Fahrschule mit einer Gruppe von mindestens sechs, höchstens zwölf Teilnehmern durchgeführt und besteht aus fünf Teilen: vier Theorie-Sitzungen von jeweils 135 Minuten Dauer und einer Beobachtungsfahrt zwischen der ersten und der zweiten Sitzung, welche mindestens 30 Minuten dauert und mit jeweils bis zu drei Teilnehmern stattfindet.</p>
  <p>Im Rahmen des Aufbauseminars werden unter anderem die Verstöße der Teilnehmer besprochen und Wege zur zukünftigen Vermeidung gesucht.</p>
  <p>Mit Abschluss des Seminars erhalten die Teilnehmer eine Bescheinigung, die bei der entsprechenden Verwaltungsbehörde eingereicht werden muss.</p>
  <p>Wird das Seminar vom Führerscheininhaber in der von der Verwaltungsbehörde festgesetzen Frist nicht erfolgreich abgeschlossen, wird die Fahrerlaubnis entzogen. Eine neue Fahrerlaubnis wird erst erteilt wenn die Teilnahme an einem Ausbauseminar nachgewiesen wird.</p>
</div>

<div class="card" style="left:101px;top:3391px;width:1000px;height:623px"></div>
<div class="abs" style="left:172px;top:3450px;font-size:32px;font-weight:600;color:var(--ink)">Kontaktieren Sie uns</div>
<div class="abs" style="left:172px;top:3508px;width:380px;font-size:14.5px;line-height:27.5px">Haben Sie Fragen oder möchten Sie weitere Informationen?<br>Wir stehen Ihnen gerne zur Verfügung! Kontaktieren Sie uns über das</div>
<div class="info" style="top:3650px">
  <svg width="18" height="24" viewBox="0 0 18 24"><path d="M9 0C4 0 0 4 0 9c0 7 9 15 9 15s9-8 9-15c0-5-4-9-9-9zm0 12.5A3.5 3.5 0 1 1 9 5.5a3.5 3.5 0 0 1 0 7z" fill="#3b3b3b"/></svg>
  <span>An der Talstraße 12<br>in 09100 Lindenau /OT Birkwald</span>
</div>
<div class="info" style="top:3700px">
  <svg width="16" height="16" viewBox="0 0 24 24"><path d="M6.6 10.8a15 15 0 0 0 6.6 6.6l2.2-2.2c.3-.3.7-.4 1-.2 1.1.4 2.3.6 3.6.6.6 0 1 .4 1 1V20c0 .6-.4 1-1 1A17 17 0 0 1 3 4c0-.6.4-1 1-1h3.5c.6 0 1 .4 1 1 0 1.3.2 2.5.6 3.6.1.3 0 .7-.2 1z" fill="#3b3b3b"/></svg>
  <span>+49 000 5550123-0</span>
</div>
<div class="info" style="top:3740px">
  <svg width="18" height="14" viewBox="0 0 18 14"><rect width="18" height="14" rx="1.5" fill="#3b3b3b"/><path d="M2 2l7 5.5L16 2" stroke="#fff" stroke-width="1.6" fill="none"/></svg>
  <span>info@fahrschule-brandhoff.de</span>
</div>
<div class="info" style="top:3781px">
  <svg width="18" height="18" viewBox="0 0 18 18"><circle cx="9" cy="9" r="9" fill="#3b3b3b"/><path d="M9 4v5.5l3.5 2" stroke="#fff" stroke-width="1.6" fill="none"/></svg>
  <span>Mo - Fr 9.00 - 17.00 Uhr</span>
</div>
<div class="social" style="left:177px"></div>
<div class="social" style="left:228px"></div>
<div class="social" style="left:280px"></div>

<div class="green-head" style="left:610px;top:3453px;font-size:32px">Haben Sie Frage</div>
<div class="label" style="left:610px;top:3500px">Fullname</div>
<div class="field" style="left:610px;top:3533px;width:425px;height:36px;padding:0"></div>
<div class="label" style="left:610px;top:3585px">Email</div>
<div class="label" style="left:837px;top:3585px">Telefonnummer</div>
<div class="field" style="left:610px;top:3617px;width:198px;height:36px;padding:0"></div>
<div class="field" style="left:837px;top:3617px;width:198px;height:36px;padding:0"></div>
<div class="label" style="left:610px;top:3668px">Message</div>
<div class="field" style="left:610px;top:3701px;width:425px;height:136px;color:#e4e4e4;padding:10px 16px">Note</div>
<div class="btn" style="left:878px;top:3865px;width:154px;height:38px">Senden</div>

<div class="brand" style="left:105px;top:4080px"><b>Brandhoff</b>Fahrschule</div>
<nav class="footer-nav"><span>Home</span><span>Anmeldung</span><span>Über uns</span><span>Preisliste</span><span>Kontakt</span><span>Impressum</span><span>Datenschutzerklärung</span></nav>
<footer class="bar">Copyrights</footer>

</body>
</html>
```